依頼詳細
弊社ホームページを参考にデザインして頂き干支を入れ
来年以降力を入れていきたい商材(回線事業 ミナモ光)(蓄電池)をどこかに入れたいです
記載項目
(株) ミナモ事務機
530-0047 大阪市北区西天満4-9-22
TEL 06-6418-2275 FAX 06-6418-2276
http://www.minamojimuki.example.jp
希望イメージ
シンプル 複雑
単色 カラフル
暗い 明るい
日常 高級
遊び心 厳粛
未来的 伝統的
女性的 男性的
希望する色
青系
納品ファイル
補足説明
年賀状のデザインをご提案ください
■ 選んだ理由

シンプルで良いデザインでした
社員の投票で最終決定させていただきました

■ 提案者全員のお礼・コメント

沢山ご提案頂きありがとうございました
最後なかなか決めきれず社員の投票になりましたが
素晴らしいご提案がたくさんございました
ありがとうございます。

```html
<!DOCTYPE html>
<html lang="ja">
<head>
<meta charset="utf-8">
<title>謹賀新年 ミナモ事務機</title>
<link rel="stylesheet" href="https://fonts.googleapis.com/css2?family=Noto+Sans+JP:wght@400;500;700;900&display=swap">
<style>
  :root {
    --navy: #1d2f5e;
    --blue: #2b62b8;
    --red: #d3202a;
    --paper: #ffffff;
    --line: #c9cdd4;
    --ink-soft: #3b4868;
  }
  html, body { margin: 0; padding: 0; overflow: hidden; background: #eef0f3; }
  .card {
    position: relative;
    width: 886px; height: 1200px;
    background: var(--paper);
    box-sizing: border-box;
    border: 2px solid var(--line);
    overflow: hidden;
    font-family: "Noto Sans JP", sans-serif;
    color: var(--navy);
  }
  .greeting {
    position: absolute; top: 110px; left: 0; width: 100%;
    text-align: center; margin: 0;
    font-size: 104px; font-weight: 900; letter-spacing: 12px; line-height: 1.4;
    color: var(--navy);
  }
  .greeting .accent { color: var(--red); }
  .announce {
    position: absolute; top: 288px; left: 0; width: 100%;
    text-align: center; font-size: 20px; font-weight: 500; color: var(--blue);
    letter-spacing: 2px;
  }
  .product {
    position: absolute; top: 318px; left: 0; width: 100%;
    text-align: center; font-size: 36px; font-weight: 900; color: var(--navy);
  }
  .product-note {
    position: absolute; top: 366px; left: 0; width: 100%;
    text-align: center; font-size: 17px; font-weight: 500; color: var(--ink-soft);
  }
  .brand {
    position: absolute; top: 500px; left: 0; width: 100%;
    display: flex; align-items: center; justify-content: center; gap: 22px;
  }
  .brand-square { width: 64px; height: 64px; background: var(--navy); flex: none; }
  .brand-name {
    font-family: "Noto Sans JP", sans-serif;
    font-size: 38px; font-weight: 700; letter-spacing: 2px; line-height: 1;
    color: var(--navy);
  }
  .url {
    position: absolute; top: 664px; left: 0; width: 100%;
    text-align: center; font-size: 17px; color: var(--ink-soft);
  }
  .skyline {
    position: absolute; top: 705px; left: 0; width: 100%; height: 340px;
    background: linear-gradient(180deg, #e7eff8 0%, #b9cce0 45%, #7f97b4 75%, #5f7898 100%);
  }
  .bands { position: absolute; top: 705px; left: 0; width: 886px; height: 495px; }
  .footer {
    position: absolute; left: 0; bottom: 0; width: 100%; height: 170px;
    color: #fff;
  }
  .company {
    position: absolute; left: 70px; bottom: 118px;
    font-size: 25px; font-weight: 700;
  }
  .address {
    position: absolute; left: 300px; bottom: 122px;
    font-size: 16px; font-weight: 500;
  }
  .contact {
    position: absolute; left: 70px; bottom: 62px;
    font-size: 22px; font-weight: 500; letter-spacing: 1px;
  }
  .contact span + span { margin-left: 36px; }
  .zodiac {
    position: absolute; right: 80px; bottom: 110px;
    width: 110px; height: 70px; border-radius: 50%;
    background: rgba(255,255,255,0.85);
  }
</style>
</head>
<body>
<div class="card">
  <h1 class="greeting">謹賀<span class="accent">新</span>年</h1>
  <div class="announce">― 回線事業はじめました ―</div>
  <div class="product">ミナモ光サポートパッケージ</div>
  <div class="product-note">回線から通信機器までワンストップサービス</div>

  <div class="brand">
    <div class="brand-square"></div>
    <div class="brand-name">MINAMO BUSINESS MACHINE</div>
  </div>

  <div class="url">http://www.minamojimuki.example.jp</div>

  <div class="skyline" role="img" aria-label="川辺に立ち並ぶ都市の高層ビル群の写真"></div>

  <svg class="bands" viewBox="0 0 886 495" aria-hidden="true">
    <polygon points="520,150 886,40 886,190 560,300" fill="#2b62b8" opacity="0.75"/>
    <polygon points="640,170 886,100 886,200 700,260" fill="#6fa3e0" opacity="0.6"/>
    <polygon points="0,300 886,210 886,495 0,495" fill="#1d2f5e"/>
  </svg>

  <div class="footer">
    <div class="company">(株) ミナモ事務機</div>
    <div class="address">〒530-0047　大阪市北区西天満4-9-22</div>
    <div class="contact"><span>TEL.06-6418-2275</span><span>FAX.06-6418-2276</span></div>
    <div class="zodiac" role="img" aria-label="干支の動物のイラスト"></div>
  </div>
</div>
</body>
</html>
```